Real Estate Website

I have a very old website that was built almost 20 years ago. We are rebuilding it and need a fresh new design for it please.
The existing website is https://northpeakhomes.example

This is for a real estate company that is selling real estate in Hokkaido, Japan (known for it's skiing and snow tourism) and is all in english as it targets westerners looking to buy holiday homes or investment properties.
Updates

Hi everyone.

Sorry this has taken so long to get back to you. My client has taken a long time to get back to me after the Christmas break.

Unfortunately they did not want to go ahead with any of the designs submitted as they said they look too much like business sales websites instead of residential and commercial sales. An example of what they lik is https://www.velmorproperty.example/
They don't want it to look at all like their business sales website (https://www.ranscombebusinesssales.example/) and have said:

• keep Ra NSCOMBE GROUP logo and color scheme the same
• Give freedom to the designers, on how what to execute what the company does.
-Commercial/Industrial
-Residential

Make them separate as there’s a different audience of clients for commercial & residential are very different.

I will provide some content and headings which you have the freedom to play around and coordinate. What I provide below are only suggestions, please feel free to be use your ideas and be innovative.

Residential listings - would like the listing to shows Features on details page.
Commercial listings – must display “building area” on the front page
HEADINGS ON TOP OF PAGE -TABS:
HOME - This MUST show on the tab
COMMERCIAL/INDUSTRIAL - This MUST show on the tab
RESIDENTIAL - This MUST show on the tab
BUSINESS SALES (this to link straight to my RANSCOMBE BUSINESS SALES & VUALUATIONS website - This MUST show on the tab
ABOUT US
BLOGS/videos- I want my team to be able to load all the videos, eg when they do videos for auctions, developments etc -– optional, if not enough space, show it on the bottom of the website ( you could also add under ABOUT US tab)
CONTACT US

Maybe show this on the home screen heading:
Specialists in Commercial/ Industrial Property,
Trusted in Residential Property

Theme:
“Maximising returns, protecting investments, expert property advisory”
Work With Us

The Information below is not in any particle order:

Book an Appraisal
Discover the Real Value of Your Property
At Ranscombe Group, we don’t just provide standard appraisals — we deliver strategic, insight-driven reports that uncover the true drivers of your property’s worth. Whether it’s commercial, industrial, or residential, our expertise ensures you see the full picture.
From market trends and rental potential to investment performance and future growth opportunities, our tailored reports give you clarity, confidence, and actionable insights.
Book a confidential consultation today and gain the expert guidance you need to maximise returns and make smarter property decisions.

What We Do
What We Do – Property Management, Sales & Leasing
At Ranscombe Group, we specialise in guiding property owners, investors, and landlords through the complexities of managing, selling, leasing, and valuing assets. Our mission is clear: to deliver clarity, confidence, and measurable results at every stage of your property journey.
We go beyond standardised reports. Our strategic, insight-driven valuations and management solutions uncover the true drivers of your property’s performance. From tailored marketing campaigns and compelling listings to confidential negotiations and introductions, we ensure your asset attracts the right tenants, buyers, or investors.
When the future of your investment is on the line, you need more than a property manager or agent — you need a partner who delivers certainty, strategy, and results. At Ranscombe Group, we don’t just manage, lease, or sell properties; we maximise value, income, and long-term growth.
Contact us today for a confidential consultation and discover how Ranscombe Group can help you achieve the strongest outcomes for your property portfolio.

Who We Are
At Ranscombe Group, we are recognised as a trusted authority in commercial and residential property management, sales, and leasing. Property owners, investors, and developers turn to us for our proven expertise, discretion, and consistent results.
Our mission is to set the standard for excellence in property services. Guided by innovation, integrity, and strategic execution, we deliver outcomes that protect assets, maximise returns, and create enduring value for our clients.
Whether your goal is to manage your investment, increase rental income, lease to the right tenants, or achieve a successful sale, we provide clarity, confidence, and tailored solutions at every stage of the journey.
Let’s begin the conversation today — and explore how Ranscombe Group can help you achieve the strongest results for your property portfolio.

Commercial & Industrial Property Management & Leasing

At Ranscombe Group, we are recognised as a leading authority in the management and leasing of premium commercial and industrial assets. Trusted by investors, landlords, and developers, our portfolio spans medical centres, healthcare facilities, allied health clinics, global franchise brands such as BWQ and The Marmalade Pantry, high‑end retail outlets, and large‑scale industrial and manufacturing properties.
We deliver strategic, results‑driven property solutions that combine market intelligence, operational excellence, and meticulous attention to detail. Our approach is designed to maximise returns, minimise vacancies, and safeguard long‑term asset performance.

Our Services
• Strategic Marketing & Leasing – Positioning your property to attract premium tenants through targeted, multi‑channel campaigns.
• Tenant & Lease Administration – Precision management of agreements, renewals, compliance, and documentation.
• Revenue Optimisation – Proactive rent collection, vacancy minimisation, and lease structuring to elevate asset value.
• Maintenance & Property Upkeep – Access to vetted, high‑quality trades for repairs and preventative care, ensuring assets remain in peak condition.
• Regulatory Compliance & Essential Services – Full oversight of statutory obligations and essential service measures, protecting both compliance and reputation.
Why Choose us
• Sector Expertise – Deep knowledge across medical, healthcare, franchise, retail, and industrial sectors, enabling tailored strategies for each asset class.
• Proactive Asset Management – Beyond operations, we actively enhance value, mitigate risk, and secure the right tenants.
• Bespoke Solutions – Every property is unique. We craft customised management and leasing strategies aligned with your objectives and market conditions.
• Professional Excellence – Integrity, precision, and industry‑leading best practices deliver measurable results and peace of mind for discerning property owners.
With Ranscombe Group, your commercial and industrial assets are managed with authority, insight, and excellence — ensuring performance that meets the expectations of high‑end investors and developers.

```html
<!DOCTYPE html>
<html lang="en">
<head>
<meta charset="utf-8">
<title>North Peak Homes</title>
<link href="https://fonts.googleapis.com/css2?family=Inter:wght@400;500;600;700&family=Libre+Baskerville:wght@400;700&display=swap" rel="stylesheet">
<style>
:root{
  --red:#c8202a;
  --red-dark:#a8161f;
  --ink:#1b1b1b;
  --text:#444;
  --muted:#777;
  --line:#bdbdbd;
  --grey:#f1f1f1;
  --white:#fff;
  --black:#050505;
  --serif:"Libre Baskerville", Georgia, serif;
  --sans:"Inter", Arial, sans-serif;
}
*{box-sizing:border-box;margin:0;padding:0}
html,body{width:1200px;height:4702px;overflow:hidden;background:var(--white)}
body{position:relative;font-family:var(--sans);color:var(--ink)}
.abs{position:absolute}
.btn{position:absolute;display:flex;align-items:center;justify-content:center;gap:10px;border-radius:4px;font-weight:600;font-size:13px}
.btn-red{background:var(--red);color:var(--white)}
.btn-outline{border:1px solid var(--line);color:var(--ink);background:var(--white)}
.eyebrow{font-size:20px;color:var(--red);letter-spacing:.5px}
.h-serif{font-family:var(--serif);font-weight:700;color:var(--ink);text-transform:uppercase}

/* header */
.site-header{position:absolute;left:0;top:0;width:1200px;height:92px;background:var(--white)}
.brand{left:142px;top:30px;display:flex;align-items:center;gap:10px}
.brand-mark{width:30px;height:30px;border-radius:50%;background:var(--red)}
.brand-name{font-family:var(--serif);font-size:18px;color:var(--ink);letter-spacing:1px;white-space:nowrap}
.call{right:144px;top:14px;display:flex;align-items:center;gap:10px;font-size:14px}
.call-icon{width:30px;height:30px;border-radius:50%;background:var(--red);display:flex;align-items:center;justify-content:center}
.call b{color:var(--red);font-weight:500}
.nav{right:144px;top:58px;display:flex;gap:22px;font-size:14px;white-space:nowrap}
.nav a{display:block;color:var(--ink);text-decoration:none;position:relative}
.nav a.active{color:var(--red)}
.nav a.active::before{content:"";position:absolute;left:50%;top:-9px;width:26px;height:3px;margin-left:-13px;background:var(--red)}

/* hero */
.hero-svg{left:0;top:92px}
.hero-tag{left:336px;top:237px;width:526px;height:52px;background:var(--red);color:var(--white);font-weight:700;font-size:27px;display:flex;align-items:center;justify-content:center;border-radius:4px}
.hero-title{left:0;width:1200px;top:306px;text-align:center;font-family:var(--serif);font-weight:700;font-size:53px;color:#12203a}
.search-tab{left:484px;top:393px;width:232px;height:46px;background:rgba(255,255,255,.75);border:2px solid rgba(255,255,255,.9);border-bottom:none;border-radius:10px 10px 0 0;display:flex;align-items:center;justify-content:center;font-weight:600;font-size:21px;color:#222}
.search-panel{left:210px;top:424px;width:780px;height:170px;background:rgba(255,255,255,.28);border:2px solid rgba(255,255,255,.9);border-radius:12px}
.field{position:absolute;top:40px;width:178px}
.field label{display:block;font-size:13px;color:#222;margin-bottom:6px}
.field .select{height:38px;background:var(--white);border-radius:4px;position:relative}
.field .select::after{content:"";position:absolute;right:10px;top:11px;width:14px;height:14px;border-radius:50%;border:1px solid #888}
.find-btn{left:300px;top:107px;width:178px;height:38px}
.scroll-down{left:540px;top:694px;width:120px;height:70px}

/* welcome */
.welcome-photo{left:144px;top:946px;width:373px;height:396px;border-radius:10px;background:linear-gradient(180deg,#5c82c2 0%,#9bb3d8 35%,#8a4a3a 55%,#e9edf2 100%)}
.welcome-inset{left:369px;top:1161px;width:190px;height:239px;border-radius:12px;background:var(--white);padding:8px;box-shadow:0 4px 16px rgba(0,0,0,.12)}
.welcome-inset div{width:100%;height:100%;border-radius:8px;background:linear-gradient(180deg,#2f5fb0 0%,#8fb0df 40%,#d0d8e4 65%,#f4f6f9 100%)}
.welcome-copy{left:599px;top:944px;width:457px}
.welcome-copy h2{font-size:44px;line-height:48px;margin:12px 0 18px}
.welcome-copy p{font-size:14px;line-height:24px;color:var(--text);text-align:justify;margin-bottom:18px}

/* featured */
.featured-eyebrow{left:0;width:1200px;top:1672px;text-align:center;color:var(--white)}
.featured-title{left:0;width:1200px;top:1702px;text-align:center;font-family:var(--serif);font-weight:700;font-size:44px;color:var(--white)}
.category-tabs{left:0;width:1200px;top:1764px;display:flex;justify-content:center;gap:10px}
.category-tabs span{height:32px;padding:0 18px;border:1px solid rgba(255,255,255,.8);border-radius:16px;color:var(--white);font-size:13px;font-weight:600;display:flex;align-items:center}
.category-tabs span.active{background:var(--white);color:var(--red)}
.card{position:absolute;top:1811px;width:288px;height:442px;background:var(--white);border-radius:10px;overflow:hidden}
.card-photo{height:223px}
.card-tag{position:absolute;left:14px;top:14px;height:24px;padding:0 10px;background:var(--red);color:var(--white);font-size:11px;font-weight:700;border-radius:3px;display:flex;align-items:center;letter-spacing:.5px}
.card h3{text-align:center;font-size:19px;font-weight:600;margin-top:28px}
.card .price{text-align:center;font-size:21px;font-weight:600;color:var(--red);margin-top:8px}
.specs{display:flex;justify-content:center;gap:26px;margin-top:14px;font-size:15px}
.specs span{display:flex;align-items:center;gap:10px}
.specs i{display:block;width:18px;height:12px;background:var(--ink);border-radius:3px}
.building-area{text-align:center;margin-top:14px;font-size:15px;color:var(--text)}
.building-area b{color:var(--ink);font-weight:600}
.card .btn{left:67px;top:375px;width:154px;height:40px}
.ribbon{position:absolute;right:-38px;top:22px;width:150px;height:22px;background:var(--red);color:var(--white);font-size:11px;font-weight:700;text-align:center;line-height:22px;transform:rotate(45deg)}
.slider-arrow{top:2024px}

/* tips */
.tips-copy{left:144px;top:2590px;width:430px}
.tips-copy h2{font-size:44px;margin:8px 0 14px}
.tips-list{list-style:none;font-size:14px;color:var(--text);line-height:20px}
.tips-list li{display:flex;gap:14px;margin-bottom:20px}
.tips-list li svg{flex:none;margin-top:1px}
.tips-btn{left:144px;top:2975px;width:155px;height:38px}

/* contact */
.contact-eyebrow{left:0;width:1200px;top:3206px;text-align:center}
.contact-title{left:0;width:1200px;top:3242px;text-align:center;font-size:44px}
.contact-item{position:absolute;top:3328px;width:300px;text-align:center}
.contact-item .pin{width:74px;height:74px;margin:0 auto;border-radius:50%;background:var(--red);display:flex;align-items:center;justify-content:center}
.contact-item .label{font-size:18px;color:#555;margin-top:16px}
.contact-item .value{font-size:18px;font-weight:600;margin-top:12px}
.input{position:absolute;border:1.5px solid #888;border-radius:8px;font-size:18px;color:#444;padding:24px 26px}
.submit-btn{left:502px;top:3813px;width:196px;height:48px;font-size:17px}

/* footer */
.footer-svg{left:0;top:3900px}
.footer-col{position:absolute;top:4392px;color:var(--white)}
.footer-col h4{font-size:19px;font-weight:600;margin-bottom:14px}
.footer-col ul{list-style:none;font-size:13px;line-height:22.4px}
.footer-col li::before{content:"»";margin-right:14px}
.newsletter-input{width:253px;height:50px;border:1.5px solid var(--white);border-radius:6px;display:flex;align-items:center;gap:12px;padding-left:24px;font-size:13px}
.newsletter-input i{display:block;width:14px;height:10px;background:var(--white);border-radius:1px}
.subscribe{position:static;margin-top:14px;width:253px;height:46px;font-size:13px}
.touch-row{display:flex;align-items:center;gap:12px;font-size:13px;font-weight:600;margin-bottom:8px}
.touch-row i{display:block;width:10px;height:10px;background:var(--red);border-radius:2px}
.socials{display:flex;gap:14px;margin-top:28px}
.socials span{width:34px;height:34px;border-radius:50%;background:#333}
.socials span.on{background:var(--red)}
.footer-rule{left:144px;top:4614px;width:912px;height:1px;background:#333}
.copyright{left:0;width:1200px;top:4646px;text-align:center;color:var(--white);font-size:14px}
</style>
</head>
<body>

<!-- header -->
<header class="site-header">
  <div class="abs brand"><span class="brand-mark"></span><span class="brand-name">NORTH PEAK HOMES</span></div>
  <div class="abs call">
    <span class="call-icon"><svg width="14" height="14" viewBox="0 0 24 24"><path fill="#fff" d="M6.6 10.8a15 15 0 006.6 6.6l2.2-2.2c.3-.3.7-.4 1-.2 1.1.4 2.3.6 3.6.6.6 0 1 .4 1 1V20c0 .6-.4 1-1 1A17 17 0 013 4c0-.6.4-1 1-1h3.5c.6 0 1 .4 1 1 0 1.2.2 2.4.6 3.6.1.3 0 .7-.2 1z"/></svg></span>
    <span>Call Us! <b>+81 136 55 0142</b></span>
  </div>
  <nav class="abs nav">
    <a class="active">Home</a><a>Commercial/Industrial</a><a>Residential</a><a>Business Sales</a><a>About Us</a><a>Contact Us</a>
  </nav>
</header>

<!-- hero -->
<svg class="abs hero-svg" width="1200" height="780" viewBox="0 92 1200 780">
  <defs>
    <linearGradient id="heroSky" x1="0" y1="0" x2="0" y2="1">
      <stop offset="0" stop-color="#8fbfe8"/>
      <stop offset=".3" stop-color="#c9d9e8"/>
      <stop offset=".5" stop-color="#8c9cb0"/>
      <stop offset=".8" stop-color="#4b5a70"/>
      <stop offset="1" stop-color="#3a4456"/>
    </linearGradient>
  </defs>
  <path d="M0 92H1200V555C1100 750 850 825 600 825C340 825 130 760 0 610Z" fill="url(#heroSky)" role="img" aria-label="Snowy Sapporo city skyline with mountains"/>
  <path d="M22 612C130 760 340 850 600 850C680 850 740 842 800 828C730 838 660 842 600 842C360 842 160 770 40 640Z" fill="#c8202a"/>
</svg>
<div class="abs hero-tag">WHERE EXCEPTIONAL PROPERTIES</div>
<h1 class="abs hero-title">MEET EXCEPTIONAL PEOPLE</h1>
<div class="abs search-panel">
  <div class="field" style="left:18px"><label>Bedrooms</label><div class="select"></div></div>
  <div class="field" style="left:205px"><label>Bathrooms</label><div class="select"></div></div>
  <div class="field" style="left:393px"><label>Property type</label><div class="select"></div></div>
  <div class="field" style="left:580px"><label>Location</label><div class="select"></div></div>
  <div class="btn btn-red find-btn">Find Properties</div>
</div>
<div class="abs search-tab">Property Search</div>
<svg class="abs scroll-down" viewBox="0 0 120 70">
  <path d="M60 2V38M50 28L60 38L70 28" stroke="#fff" stroke-width="2" fill="none"/>
  <text x="60" y="62" text-anchor="middle" font-family="Inter, sans-serif" font-size="12" fill="#fff" transform="rotate(15 60 58)">SCROLL DOWN</text>
</svg>

<!-- red band backgrounds -->
<svg class="abs" style="left:0;top:1320px" width="1200" height="1320" viewBox="0 1320 1200 1320">
  <defs>
    <linearGradient id="redBand" x1="0" y1="0" x2="0" y2="1">
      <stop offset="0" stop-color="#c8202a"/>
      <stop offset=".5" stop-color="#b91c26"/>
      <stop offset="1" stop-color="#c8202a"/>
    </linearGradient>
  </defs>
  <path d="M0 1333C200 1500 400 1585 600 1585C800 1585 1000 1500 1200 1333V2611C1000 2450 800 2365 600 2365C400 2365 200 2450 0 2611Z" fill="url(#redBand)" role="img" aria-label="Red band with faint snowy tree silhouettes"/>
  <path d="M0 2611C200 2450 400 2365 600 2365C800 2365 1000 2450 1200 2611V2640H0Z" fill="#f1f1f1"/>
</svg>
<div class="abs" style="left:0;top:2640px;width:1200px;height:492px;background:var(--grey)"></div>

<!-- welcome -->
<div class="abs welcome-photo" role="img" aria-label="Red brick warehouse in snow under a blue sky"></div>
<div class="abs welcome-inset"><div role="img" aria-label="Snowy house with a for sale sign and a mountain behind"></div></div>
<div class="abs welcome-copy">
  <div class="eyebrow">WELCOME TO</div>
  <h2 class="h-serif">North Peak<br>Homes</h2>
  <p>An investment in Hokkaido property offers tremendous potential for both lifestyle and financial returns. But, the market is complex and dynamic. To invest wisely you need advice on all the potential pitfalls.</p>
  <p>The North Peak Homes team is small and dedicated group of professionals focused on delivering the best outcome for our clients whilst never compromising our ethical standards. As a result, we have some very loyal and long-time clients whom we have assisted to buy and sell properties for more than 15 years.</p>
</div>
<div class="btn btn-red" style="left:599px;top:1349px;width:155px;height:39px">Learn More <svg width="22" height="10" viewBox="0 0 22 10"><path d="M0 5H20M16 1L20 5L16 9" stroke="#fff" stroke-width="1.5" fill="none"/></svg></div>

<!-- featured -->
<div class="abs eyebrow featured-eyebrow">OUR PROPERTIES</div>
<h2 class="abs featured-title">FEATURED PROPERTIES</h2>
<div class="abs category-tabs"><span class="active">Residential</span><span>Commercial / Industrial</span></div>

<svg class="abs slider-arrow" style="left:58px" width="30" height="20" viewBox="0 0 30 20"><path d="M30 10H2M10 2L2 10L10 18" stroke="#fff" stroke-width="2" fill="none"/></svg>
<svg class="abs slider-arrow" style="left:1112px" width="30" height="20" viewBox="0 0 30 20"><path d="M0 10H28M20 2L28 10L20 18" stroke="#fff" stroke-width="2" fill="none"/></svg>

<article class="card" style="left:144px">
  <div class="card-photo" style="background:linear-gradient(180deg,#e6e8ec,#b99a7a 55%,#f3f4f6)" role="img" aria-label="Wooden house with deep snow on the roof"></div>
  <span class="card-tag">RESIDENTIAL</span>
  <h3>Enormous House</h3>
  <div class="price">¥ 39,000,000</div>
  <div class="specs"><span><i></i>7</span><span><i></i>4</span><span><i></i>2</span></div>
  <div class="btn btn-outline">Full Details <svg width="22" height="10" viewBox="0 0 22 10"><path d="M0 5H20M16 1L20 5L16 9" stroke="#c8202a" stroke-width="1.5" fill="none"/></svg></div>
</article>
<article class="card" style="left:455px">
  <div class="card-photo" style="background:linear-gradient(180deg,#d7dadf,#8d9097 55%,#eceef0)" role="img" aria-label="Historic white building with a tower in winter"></div>
  <span class="card-tag">RESIDENTIAL</span>
  <div class="ribbon">SOLD OUT</div>
  <h3>Enormous House</h3>
  <div class="price">¥ 16,000,000</div>
  <div class="specs"><span><i></i>3</span><span><i></i>2</span><span><i></i>1</span></div>
  <div class="btn btn-red">Full Details <svg width="22" height="10" viewBox="0 0 22 10"><path d="M0 5H20M16 1L20 5L16 9" stroke="#fff" stroke-width="1.5" fill="none"/></svg></div>
</article>
<article class="card" style="left:767px">
  <div class="card-photo" style="background:linear-gradient(180deg,#3f6fbf,#a9b8cc 45%,#7a5a4a 70%,#e8ebef)" role="img" aria-label="Hotel buildings in a snowy valley"></div>
  <span class="card-tag">COMMERCIAL</span>
  <h3>Resort Hotel Building</h3>
  <div class="price">¥11,250,000</div>
  <div class="building-area">Building area <b>1,240 m²</b></div>
  <div class="btn btn-outline">Full Details <svg width="22" height="10" viewBox="0 0 22 10"><path d="M0 5H20M16 1L20 5L16 9" stroke="#c8202a" stroke-width="1.5" fill="none"/></svg></div>
</article>

<!-- tips -->
<div class="abs tips-copy">
  <div class="eyebrow">TIPS</div>
  <h2 class="h-serif">Buying Tips</h2>
  <ul class="tips-list">
    <li><svg width="18" height="18" viewBox="0 0 18 18"><circle cx="9" cy="9" r="7.5" stroke="#c8202a" stroke-width="2" fill="none"/><path d="M5 9L8 12L15 4" stroke="#c8202a" stroke-width="2" fill="none"/></svg>Is the land freehold (not all land in Niseko is freehold)?</li>
    <li><svg width="18" height="18" viewBox="0 0 18 18"><circle cx="9" cy="9" r="7.5" stroke="#c8202a" stroke-width="2" fill="none"/><path d="M5 9L8 12L15 4" stroke="#c8202a" stroke-width="2" fill="none"/></svg>What is the zoning of the land, and what implications does that have?</li>
    <li><svg width="18" height="18" viewBox="0 0 18 18"><circle cx="9" cy="9" r="7.5" stroke="#c8202a" stroke-width="2" fill="none"/><path d="M5 9L8 12L15 4" stroke="#c8202a" stroke-width="2" fill="none"/></svg>What are the building code guidelines for this area and this zoning?</li>
    <li><svg width="18" height="18" viewBox="0 0 18 18"><circle cx="9" cy="9" r="7.5" stroke="#c8202a" stroke-width="2" fill="none"/><path d="M5 9L8 12L15 4" stroke="#c8202a" stroke-width="2" fill="none"/></svg>Who is the vendor?</li>
    <li><svg width="18" height="18" viewBox="0 0 18 18"><circle cx="9" cy="9" r="7.5" stroke="#c8202a" stroke-width="2" fill="none"/><path d="M5 9L8 12L15 4" stroke="#c8202a" stroke-width="2" fill="none"/></svg>How long has the vendor owned the property?</li>
    <li><svg width="18" height="18" viewBox="0 0 18 18"><circle cx="9" cy="9" r="7.5" stroke="#c8202a" stroke-width="2" fill="none"/><path d="M5 9L8 12L15 4" stroke="#c8202a" stroke-width="2" fill="none"/></svg>Why is the vendor selling?</li>
  </ul>
</div>
<div class="btn btn-red tips-btn">Learn More <svg width="22" height="10" viewBox="0 0 22 10"><path d="M0 5H20M16 1L20 5L16 9" stroke="#fff" stroke-width="1.5" fill="none"/></svg></div>
<svg class="abs" style="left:577px;top:2600px" width="478" height="415" viewBox="0 0 478 415">
  <defs>
    <linearGradient id="tipsPhoto" x1="0" y1="0" x2="0" y2="1">
      <stop offset="0" stop-color="#c9d3de"/><stop offset=".5" stop-color="#7fa59a"/><stop offset="1" stop-color="#eef1f4"/>
    </linearGradient>
  </defs>
  <path d="M0 0H466Q478 0 478 12V403Q478 415 466 415H0C90 360 130 290 130 207C130 125 90 55 0 0Z" fill="url(#tipsPhoto)" role="img" aria-label="Green historic wooden house among bare trees in snow"/>
</svg>

<!-- contact -->
<div class="abs eyebrow contact-eyebrow">CONTACT US</div>
<h2 class="abs h-serif contact-title">Get in Touch</h2>
<div class="contact-item" style="left:146px"><div class="pin"><svg width="18" height="24" viewBox="0 0 18 24"><path d="M9 0a9 9 0 00-9 9c0 7 9 15 9 15s9-8 9-15a9 9 0 00-9-9zm0 12.5A3.5 3.5 0 119 5.5a3.5 3.5 0 010 7z" fill="#fff"/></svg></div><div class="label">Address</div><div class="value">Hokkaido, Japan</div></div>
<div class="contact-item" style="left:451px"><div class="pin"><svg width="18" height="24" viewBox="0 0 18 24"><path d="M9 0a9 9 0 00-9 9c0 7 9 15 9 15s9-8 9-15a9 9 0 00-9-9zm0 12.5A3.5 3.5 0 119 5.5a3.5 3.5 0 010 7z" fill="#fff"/></svg></div><div class="label">Email Address</div><div class="value">info@northpeakhomes.example</div></div>
<div class="contact-item" style="left:754px"><div class="pin"><svg width="18" height="24" viewBox="0 0 18 24"><path d="M9 0a9 9 0 00-9 9c0 7 9 15 9 15s9-8 9-15a9 9 0 00-9-9zm0 12.5A3.5 3.5 0 119 5.5a3.5 3.5 0 010 7z" fill="#fff"/></svg></div><div class="label">Phone</div><div class="value">+81 136 55 0142</div></div>

<div class="input" style="left:144px;top:3517px;width:291px;height:69px">Name</div>
<div class="input" style="left:455px;top:3517px;width:290px;height:69px">Email</div>
<div class="input" style="left:765px;top:3517px;width:291px;height:69px">Phone</div>
<div class="input" style="left:144px;top:3610px;width:912px;height:181px">Message</div>
<div class="btn btn-red submit-btn">Submit Now <svg width="26" height="12" viewBox="0 0 26 12"><path d="M0 6H24M19 1L24 6L19 11" stroke="#fff" stroke-width="1.8" fill="none"/></svg></div>

<!-- footer -->
<svg class="abs footer-svg" width="1200" height="802" viewBox="0 3900 1200 802">
  <defs>
    <linearGradient id="citySky" x1="0" y1="0" x2="0" y2="1">
      <stop offset="0" stop-color="#ffffff"/><stop offset=".2" stop-color="#b9cce0"/><stop offset=".55" stop-color="#5f7fa6"/><stop offset="1" stop-color="#2e3f5a"/>
    </linearGradient>
  </defs>
  <rect x="0" y="3900" width="1200" height="560" fill="url(#citySky)" role="img" aria-label="Misty city view with mountains in the distance"/>
  <path d="M0 4425C200 4240 420 4160 620 4160C860 4160 1050 4230 1200 4350V4702H0Z" fill="#050505"/>
  <path d="M560 4163C800 4150 1020 4210 1200 4355V4392C1040 4250 820 4176 560 4163Z" fill="#c8202a"/>
  <path d="M0 4418C180 4250 380 4170 560 4163C390 4190 200 4270 0 4440Z" fill="#ffffff" opacity=".9"/>
</svg>

<div class="footer-col" style="left:144px">
  <h4>Newsletter</h4>
  <div class="newsletter-input"><i></i>Email address</div>
  <div class="btn btn-red subscribe">SUBSCRIBE</div>
</div>
<div class="footer-col" style="left:471px">
  <h4>Quick Links</h4>
  <ul><li>Home</li><li>Our Story</li><li>Properties</li><li>Career</li><li>Blog</li><li>Contact</li></ul>
</div>
<div class="footer-col" style="left:655px">
  <h4>Support</h4>
  <ul><li>Get Involved</li><li>Support</li><li>Terms of Service</li><li>FAQ</li><li>Blog</li><li>Contact</li></ul>
</div>
<div class="footer-col" style="left:867px">
  <h4>Get in Touch</h4>
  <div class="touch-row"><i></i>+1 888 888 8888</div>
  <div class="touch-row"><i></i>info@companyname.com</div>
  <div class="socials"><span class="on"></span><span></span></div>
</div>
<div class="abs footer-rule"></div>
<div class="abs copyright">© Copyrights 2026 | All Rights Reserved</div>

</body>
</html>
```